Realtor needs 8 1/2 x 11 flyer designed both sides

I uploaded a new word doc to be used under each of the pictures on the front page.

Colors

Designer to choose colors to be used in the design.

```html
<!DOCTYPE html>
<html lang="en">
<head>
<meta charset="utf-8">
<title>Realtor Flyer – Front and Back</title>
<link href="https://fonts.googleapis.com/css2?family=Cinzel:wght@500;600&family=Montserrat:wght@400;500&display=swap" rel="stylesheet">
<style>
  :root {
    --backdrop: #262626;
    --paper: #ffffff;
    --brand-blue: #2f4fb0;
    --panel-blue: #3a64c4;
    --panel-blue-deep: #2d52ad;
    --ink: #4a4a4a;
    --on-blue: #ffffff;
    --rule: #8fa8e6;
  }
  * { margin: 0; padding: 0; box-sizing: border-box; }
  html, body { width: 1200px; height: 1200px; overflow: hidden; background: var(--backdrop); }
  .sheet { position: absolute; background: var(--paper); box-shadow: 0 4px 10px rgba(0,0,0,.45); overflow: hidden; }
  .front { left: 66px; top: 50px; width: 506px; height: 709px; }
  .back  { left: 616px; top: 443px; width: 504px; height: 707px; background: linear-gradient(160deg, var(--panel-blue) 0%, var(--panel-blue-deep) 100%); }
  .photo { position: absolute; }

  /* front */
  .agent-portrait { left: 32px; top: 510px; width: 144px; height: 194px; background: linear-gradient(180deg, #f2ede6 0%, #d9c7a2 45%, #1e1e22 100%); }
  .brand-lockup { position: absolute; left: 300px; top: 580px; width: 170px; display: flex; align-items: center; justify-content: center; gap: 8px; }
  .brand-square { width: 14px; height: 14px; background: var(--brand-blue); flex: none; }
  .brand-name { font-family: 'Cinzel', serif; font-weight: 500; font-size: 17px; color: var(--brand-blue); letter-spacing: 1px; white-space: nowrap; }
  .agent-name { position: absolute; left: 282px; top: 618px; font-family: 'Cinzel', serif; font-weight: 600; font-size: 25px; color: var(--brand-blue); letter-spacing: .5px; white-space: nowrap; }
  .brokerage-mark { position: absolute; left: 283px; top: 655px; width: 26px; height: 26px; border-radius: 50%; background: var(--brand-blue); }
  .agent-details { position: absolute; left: 321px; top: 650px; font-family: 'Montserrat', sans-serif; font-size: 11.5px; line-height: 16.5px; color: var(--ink); }

  /* back */
  .hero { left: 0; top: 0; width: 504px; height: 126px; background: linear-gradient(90deg, #6f86b8 0%, #3c3c55 45%, #7a5a4a 70%, #b08c86 100%); }
  .title-band { position: absolute; left: 0; top: 126px; width: 504px; height: 34px; background: var(--paper); text-align: center; font-family: 'Cinzel', serif; font-weight: 600; font-size: 27px; line-height: 36px; color: var(--brand-blue); letter-spacing: .5px; }
  .bio-name { position: absolute; font-family: 'Cinzel', serif; font-weight: 500; font-size: 15px; color: var(--on-blue); white-space: nowrap; }
  .bio-details { position: absolute; font-family: 'Montserrat', sans-serif; font-size: 8.6px; line-height: 12.3px; color: var(--on-blue); }
  .bio-text { position: absolute; font-family: 'Montserrat', sans-serif; font-size: 9.3px; line-height: 12.3px; color: var(--on-blue); }
  .bio-text p + p { margin-top: 12px; }
  .bio-text.justified { text-align: justify; }
  .portrait-frame { position: absolute; border: 3px solid var(--paper); }
  .section-rule { position: absolute; left: 24px; top: 425px; width: 456px; height: 2px; background: linear-gradient(90deg, transparent, var(--rule), transparent); }
</style>
</head>
<body>

<section class="sheet front">
  <div class="photo" style="left:0;top:2px;width:251px;height:244px;background:linear-gradient(180deg,#8ec3ee 0%,#d9c9b0 45%,#6d9a3e 100%)" role="img" aria-label="Covered back patio with table and chairs beside a lawn"></div>
  <div class="photo" style="left:254px;top:2px;width:126px;height:120px;background:linear-gradient(180deg,#3d7fd6 0%,#c9c2b6 40%,#2fc4e0 70%,#c8c2bb 100%)" role="img" aria-label="Backyard swimming pool"></div>
  <div class="photo" style="left:383px;top:2px;width:123px;height:120px;background:linear-gradient(180deg,#f2f0ec 0%,#b8a58a 50%,#5d6f3c 100%)" role="img" aria-label="Stone house entrance with arched portico"></div>
  <div class="photo" style="left:254px;top:126px;width:126px;height:121px;background:linear-gradient(180deg,#9fc6ee 0%,#e2d6b8 50%,#8da05a 100%)" role="img" aria-label="Two-story home with front steps"></div>
  <div class="photo" style="left:383px;top:126px;width:123px;height:121px;background:linear-gradient(180deg,#a9c7ea 0%,#9a8f7a 45%,#4f8a35 100%)" role="img" aria-label="Craftsman cottage with garden path"></div>
  <div class="photo" style="left:0;top:249px;width:122px;height:121px;background:linear-gradient(180deg,#c58aa8 0%,#d6b48a 45%,#55703a 100%)" role="img" aria-label="Two-story home at sunset"></div>
  <div class="photo" style="left:125px;top:249px;width:126px;height:121px;background:linear-gradient(180deg,#b9b2a3 0%,#d8d1bf 55%,#7a8b4c 100%)" role="img" aria-label="House front with bay window"></div>
  <div class="photo" style="left:254px;top:249px;width:252px;height:244px;background:linear-gradient(180deg,#4e86d8 0%,#a9c8ec 35%,#c8bba4 55%,#5fae38 80%,#cfcfcf 100%)" role="img" aria-label="Single-story ranch home with driveway and lawn"></div>
  <div class="photo" style="left:0;top:372px;width:122px;height:121px;background:linear-gradient(180deg,#7fb0e8 0%,#d9cbb4 50%,#8aa35a 100%)" role="img" aria-label="Home with garage and driveway"></div>
  <div class="photo" style="left:125px;top:372px;width:126px;height:121px;background:linear-gradient(180deg,#d9e6f2 0%,#e8e3da 45%,#5f9a3f 100%)" role="img" aria-label="White cottage with turret and curved walkway"></div>

  <div class="photo agent-portrait" role="img" aria-label="Portrait of the realtor"></div>
  <div class="brand-lockup"><span class="brand-square"></span><span class="brand-name">BELLINI HOMES</span></div>
  <div class="agent-name">LAURA BELLINI</div>
  <div class="brokerage-mark"></div>
  <div class="agent-details">Realtor<br>Laura@Laurabhomes.com<br>DRE # 01234567</div>
</section>

<section class="sheet back">
  <div class="photo hero" role="img" aria-label="Evening view of a modern home with pool terrace and lounge chairs"></div>
  <div class="title-band">WHY CHOOSE US?</div>

  <div class="bio-name" style="left:25px;top:186px">LAURA BELLINI</div>
  <div class="bio-details" style="left:25px;top:206px">Realtor®<br>555.214.6730<br>Laura@Laurabhomes.com<br>DRE# 01234567</div>
  <div class="bio-text" style="left:159px;top:182px;width:318px">
    <p>I know many of you, but for those whom I dom not, I'd like to introduce myself. I've been a resident of Harbor Hills for almost 23 years. I've loved our neighborhood from the first time I discovered it. From our beautiful parks to our fabulous pool and amenities, it's hard to beat our wonderful community.</p>
    <p>I always say where we live is the next best thing to living on a tropical island. I've traveled to many and I'm always happy to come back to my Harbor Hills home. My passion for this area is ts why I'm in Real Estate. I consider myself incredibly fortunate to sell homes and help people purchase homes in an area that I love with all my heart.</p>
    <p>Marta and I have been close colleagues for the last 8 years, both working as Realtors and long time residents of Harbor Hills. I am most grateful for our working relationship and the friendship we have formed. I am humbled by her trust and respect for me. Please feel welcome to call on me for all things home-related. I will look forward to meeting you!</p>
  </div>
  <div class="photo portrait-frame" style="left:24px;top:274px;width:114px;height:137px;background:linear-gradient(180deg,#f4f1ec 0%,#d9c7a2 45%,#1e1e22 100%)" role="img" aria-label="Portrait of the realtor"></div>

  <div class="section-rule"></div>

  <div class="bio-text justified" style="left:25px;top:443px;width:318px">
    <p>I have exciting and bittersweet news I want to share with my Harbor Hills clients, friends and neighbors. After 40 (something) years in the Real Estate business, I have decided to retire. Some of you may last month I sold my Harbor Hills home and moved to the beautiful Willow Glen community in Rancho Sierra. My husband and I wanted to scale down and have time to enjoy retirement, together. I have been so blessed to have had an illustrious career in Real Estate and I want to thank you with a most grateful heart for giving me the opportunity to work with you. I have enjoyed every minute.</p>
    <p>I'm happy and proud to be turning my business over to Laura Bellini, fellow Keystone Realty Agent. She and I have enjoyed a very close working relationship for many years and there is nobody else except Laura I'd consider turning my business over to. Laura is.. I will add verbiage here conveying your thoughts about me. Please contact me if you'd like a personal introduction to Laura or contact her firectly. Remember to mention me when you contact Laura and let her know that we know each other. I wish you the very best and please say hello when you see me in the neighborhood.</p>
  </div>
  <div class="bio-name" style="right:29px;top:449px">MARTA SLOANE</div>
  <div class="bio-details" style="right:29px;top:470px;text-align:right">Realtor®<br>555.318.4429<br>Marta@MartaSloane.com<br>DRE# 00765432</div>
  <div class="photo portrait-frame" style="left:361px;top:550px;width:115px;height:136px;background:linear-gradient(180deg,#b99a6a 0%,#e6d6b8 40%,#141416 100%)" role="img" aria-label="Portrait of the retiring realtor"></div>
</section>

</body>
</html>
```